Vantage Sport And Fitness- Rates

I am opening up a new Gym/Training Facility. The Name of my New gym is Vantage Sports And Fitness. I am wanting to design a card that captures Membership Pricing/Personal Training Pricing. I will Upload the Logo. My colors are Red/Black/Silver. I really want there pricing card to "POP". IT needs to be very Professional and Clean. I will be placing these cards on a 5'7 . I would like these item on the card:
Name of Company: Vantage Sports And Fitness
Address:
2817 Larkmoor Commerce Dr.
Suite 214 Chantilly, VA 20153
Phone #: 703-555-0187
website: www.vantagesnf-example.com
Membership Rates:
$99/Month
$49 Heroes Rate
Family Plan:
2 People $149
3 People $199
4 People $299
Personal Training Rates:
1 session $102
5 sessions $490
10 sessions $940
20 sessions $1,800
40 sessions $3,400
Please be creative

```html
<!DOCTYPE html>
<html lang="en">
<head>
<meta charset="utf-8">
<title>Vantage Sports And Fitness – Rates</title>
<link href="https://fonts.googleapis.com/css2?family=Ubuntu:wght@400;500;700&family=Marcellus&display=swap" rel="stylesheet">
<style>
  :root{
    --red:#ee1c25;
    --charcoal:#4a4a4b;
    --white:#ffffff;
    --page:#eceae6;
    --photo-dark:#2a211d;
    --photo-warm:#7a5a45;
  }
  *{box-sizing:border-box;margin:0;padding:0}
  html,body{width:1200px;height:1200px;overflow:hidden;background:var(--page)}
  .rate-card{
    position:absolute;left:201px;top:40px;
    width:888px;height:1247px;
    transform:scale(0.898);transform-origin:0 0;
    background:var(--white);overflow:hidden;
    box-shadow:0 10px 30px rgba(0,0,0,.18);
    font-family:"Marcellus",serif;color:var(--white);
  }
  .hero{position:absolute;left:0;top:0;width:888px;height:660px}
  .brand{position:absolute;left:60px;top:62px;width:320px;
    font-family:"Ubuntu",sans-serif;font-weight:500;font-size:36px;line-height:42px;
    color:var(--red)}
  .rate-box{position:absolute;background:var(--charcoal);border-radius:24px;
    box-shadow:0 8px 14px rgba(0,0,0,.25)}
  .rate-box h2{position:absolute;left:25px;right:25px;top:10px;height:48px;border-radius:24px;
    background:var(--red);font-family:"Ubuntu",sans-serif;font-weight:500;font-size:28px;
    text-align:center;line-height:48px;color:var(--white);white-space:nowrap}
  .membership{left:52px;top:676px;width:371px;height:169px}
  .family{left:52px;top:868px;width:371px;height:220px}
  .training{left:449px;top:676px;width:380px;height:301px}
  .rate-list{position:absolute;list-style:none;font-size:28px;line-height:43px;white-space:nowrap}
  .rate-list li{display:flex}
  .rate-list b{font-family:"Ubuntu",sans-serif;font-weight:700}
  .membership .rate-list{left:80px;top:70px}
  .family .rate-list{left:66px;top:72px}
  .family .rate-list .label{width:173px}
  .training .rate-list{left:65px;top:72px}
  .training .rate-list .label{width:174px}
  .address-band{position:absolute;left:0;top:1108px;width:888px;height:139px;background:var(--charcoal)}
  .address{position:absolute;left:95px;top:16px;font-family:"Ubuntu",sans-serif;font-size:26px;line-height:35px;font-style:normal;white-space:nowrap}
  .pin{position:absolute;left:45px;top:20px}
  .contact-panel{position:absolute;left:466px;top:1010px;width:422px;height:237px;background:var(--red);
    border-radius:120px 0 0 0 / 100px 0 0 0}
  .contact-title{position:absolute;left:65px;top:14px;font-size:29px;white-space:nowrap}
  .contact-line{position:absolute;left:30px;display:flex;align-items:center;gap:14px;white-space:nowrap}
  .contact-line.phone{top:70px;font-family:"Ubuntu",sans-serif;font-weight:700;font-size:41px}
  .contact-line.web{top:134px;font-family:"Ubuntu",sans-serif;font-size:23px}
  .icon{flex:none;width:36px;height:36px;border-radius:50%;background:var(--white);display:flex;align-items:center;justify-content:center}
</style>
</head>
<body>
<article class="rate-card">
  <svg class="hero" viewBox="0 0 888 660">
    <defs>
      <linearGradient id="photoTone" x1="0" y1="0" x2="1" y2="1">
        <stop offset="0" stop-color="var(--photo-warm)"/>
        <stop offset=".55" stop-color="#4b3a33"/>
        <stop offset="1" stop-color="var(--photo-dark)"/>
      </linearGradient>
    </defs>
    <path role="img" aria-label="Photo of two people training on indoor cycling bikes in the gym"
          d="M0 0H888V610C700 652 320 652 0 628Z" fill="url(#photoTone)"/>
    <path d="M0 628C320 652 700 652 888 610" fill="none" stroke="var(--red)" stroke-width="6"/>
    <path d="M0 0H410V90C410 145 370 180 305 180H0Z" fill="var(--white)"/>
  </svg>

  <header class="brand">Vantage Sports<br>And Fitness</header>

  <section class="rate-box membership">
    <h2>Membership Rates:</h2>
    <ul class="rate-list">
      <li><span><b>$99</b>/Month</span></li>
      <li><span><b>$49</b> Heroes Rate</span></li>
    </ul>
  </section>

  <section class="rate-box family">
    <h2>Family Plan:</h2>
    <ul class="rate-list">
      <li><span class="label">2 People</span><b>$149</b></li>
      <li><span class="label">3 People</span><b>$199</b></li>
      <li><span class="label">4 People</span><b>$299</b></li>
    </ul>
  </section>

  <section class="rate-box training">
    <h2>Personal Training Rates:</h2>
    <ul class="rate-list">
      <li><span class="label">1 session</span><span>$102</span></li>
      <li><span class="label">5 sessions</span><span>$490</span></li>
      <li><span class="label">10 sessions</span><span>$940</span></li>
      <li><span class="label">20 sessions</span><span>$1,800</span></li>
      <li><span class="label">40 sessions</span><span>$3,400</span></li>
    </ul>
  </section>

  <footer class="address-band">
    <svg class="pin" width="38" height="38" viewBox="0 0 38 38">
      <circle cx="19" cy="19" r="19" fill="var(--white)"/>
      <path d="M19 8a7 7 0 0 0-7 7c0 5 7 13 7 13s7-8 7-13a7 7 0 0 0-7-7z" fill="var(--red)"/>
      <circle cx="19" cy="15" r="2.6" fill="var(--white)"/>
    </svg>
    <address class="address">2817 Larkmoor Commerce Dr.<br>Suite 214 Chantilly, VA 20153</address>
  </footer>

  <aside class="contact-panel">
    <p class="contact-title">Contact for more info:</p>
    <p class="contact-line phone">
      <span class="icon"><svg width="22" height="22" viewBox="0 0 24 24"><path d="M6.6 10.8a15 15 0 0 0 6.6 6.6l2.2-2.2a1 1 0 0 1 1-.25 11.4 11.4 0 0 0 3.6.57 1 1 0 0 1 1 1V20a1 1 0 0 1-1 1A17 17 0 0 1 3 4a1 1 0 0 1 1-1h3.5a1 1 0 0 1 1 1c0 1.25.2 2.45.57 3.57a1 1 0 0 1-.25 1z" fill="var(--red)"/></svg></span>
      703-555-0187
    </p>
    <p class="contact-line web">
      <span class="icon"><svg width="22" height="22" viewBox="0 0 24 24"><circle cx="12" cy="12" r="9" fill="none" stroke="var(--red)" stroke-width="2"/><path d="M3 12h18M12 3c3 3 3 15 0 18M12 3c-3 3-3 15 0 18" fill="none" stroke="var(--red)" stroke-width="1.6"/></svg></span>
      www.vantagesnf-example.com
    </p>
  </aside>
</article>
</body>
</html>
```